Halvern Properties Business Cards

I would like a business card that includes myself and my partner.
Includes: Logo, office #, email, website, our names, our numbers and possibly the address. I would also like the logo to be embossed and the card to be horizontal.
There is a photo of our yard signs to give you an idea of the colors of our business.

Target Market(s)

Everyone in real estate market.
We are in a rural area. Our clientele are from all socioeconomic backgrounds.

Industry/Entity Type

Real Estate Agent

Contact Information for Business Card

Company Name: Halvern Properties
Our Names, Titles & Cell #'s : Marla Halvern-Broker (555).316.4827, Tessa Halvern-Realtor (555).627.9154
Office #: (555).841.2600
Website: halvernproperties-example.com
Joint Email: halvern@halvernproperties-example.com
Office Address: 518B W. Cottonwell Ave.
Marrowfield, OK. 70999

Font styles to use
Serif

Requirements
Must have
• HORIZONTAL, Logo, Myself and my partners names, Our cell #'s, our office #, our website, our email address
Nice to have
• Embossed logo, office address, our titles.

```html
<!DOCTYPE html>
<html lang="en">
<head>
<meta charset="utf-8">
<title>Halvern Properties Business Cards</title>
<link href="https://fonts.googleapis.com/css2?family=Libre+Baskerville:wght@700&family=Source+Sans+3:wght@400;600&display=swap" rel="stylesheet">
<style>
  :root {
    --bg: #e9e6e1;
    --card-white: #ffffff;
    --purple: #4e2a6e;
    --purple-deep: #3a1c55;
    --graphite: #4a4a4c;
    --ink-light: #ffffff;
    --shadow: rgba(0, 0, 0, 0.22);
  }
  * { margin: 0; padding: 0; box-sizing: border-box; }
  html, body {
    width: 1200px;
    height: 843px;
    overflow: hidden;
    background: var(--bg);
  }
  .stage {
    position: relative;
    width: 1200px;
    height: 843px;
    display: flex;
    align-items: center;
    justify-content: center;
    gap: 40px;
  }
  .card {
    position: relative;
    width: 560px;
    height: 320px;
    box-shadow: 0 10px 24px var(--shadow);
    overflow: hidden;
  }

  /* Front: logo card */
  .card--front {
    background: var(--card-white);
    display: flex;
    align-items: center;
    justify-content: center;
  }
  .brand {
    display: flex;
    align-items: center;
    gap: 18px;
  }
  .brand__dot {
    width: 38px;
    height: 38px;
    border-radius: 50%;
    background: var(--purple);
    flex: none;
  }
  .brand__name {
    font-family: "Libre Baskerville", serif;
    font-weight: 700;
    color: var(--purple);
    font-size: 34px;
    line-height: 1.15;
    letter-spacing: 0.02em;
  }

  /* Back: contact card */
  .card--back {
    background: linear-gradient(100deg, var(--graphite) 0%, var(--graphite) 30%, var(--purple) 55%, var(--purple-deep) 100%);
    color: var(--ink-light);
    font-family: "Source Sans 3", sans-serif;
  }
  .back__mark {
    position: absolute;
    left: 30px;
    top: 50%;
    transform: translateY(-50%);
    font-family: "Libre Baskerville", serif;
    font-weight: 700;
    color: var(--ink-light);
    font-size: 56px;
    line-height: 1.05;
  }
  .contact {
    position: absolute;
    right: 28px;
    top: 36px;
    text-align: right;
  }
  .person { margin-bottom: 10px; }
  .person__name {
    font-weight: 600;
    font-size: 19px;
    line-height: 1.15;
  }
  .person__title,
  .person__phone {
    font-size: 14px;
    line-height: 1.3;
  }
  .address {
    font-size: 14px;
    line-height: 1.3;
    margin-bottom: 12px;
  }
  .channel {
    display: flex;
    justify-content: flex-end;
    align-items: center;
    gap: 8px;
    font-size: 14px;
    line-height: 1.55;
  }
  .channel svg { width: 13px; height: 13px; fill: var(--ink-light); flex: none; }
  .channel--email { padding-right: 21px; }
</style>
</head>
<body>
<main class="stage">
  <section class="card card--front" aria-label="Business card front">
    <div class="brand">
      <span class="brand__dot" aria-hidden="true"></span>
      <div class="brand__name">Halvern<br>Properties</div>
    </div>
  </section>

  <section class="card card--back" aria-label="Business card back">
    <div class="back__mark">Halvern</div>
    <div class="contact">
      <div class="person">
        <div class="person__name">Marla Halvern</div>
        <div class="person__title">Broker</div>
        <div class="person__phone">(555).316.4827</div>
      </div>
      <div class="person">
        <div class="person__name">Tessa Halvern</div>
        <div class="person__title">Realtor</div>
        <div class="person__phone">(555).627.9154</div>
      </div>
      <div class="address">518B W. Cottonwell Ave.<br>Marrowfield, OK. 70999</div>
      <div class="channel channel--email">halvern@halvernproperties-example.com</div>
      <div class="channel">(555).841.2600
        <svg viewBox="0 0 24 24" aria-hidden="true"><path d="M6.6 10.8a15.2 15.2 0 0 0 6.6 6.6l2.2-2.2a1 1 0 0 1 1-.25 11.4 11.4 0 0 0 3.6.57 1 1 0 0 1 1 1V20a1 1 0 0 1-1 1A17 17 0 0 1 3 4a1 1 0 0 1 1-1h3.5a1 1 0 0 1 1 1c0 1.250.2 2.45.57 3.57a1 1 0 0 1-.25 1z"/></svg>
      </div>
      <div class="channel">halvernproperties-example.com
        <svg viewBox="0 0 24 24" aria-hidden="true"><path d="M2 5h20v14H2zM3.5 6.5v.4L12 12.5l8.5-5.6v-.4z"/></svg>
      </div>
      <div class="channel">
        <svg viewBox="0 0 24 24" aria-hidden="true"><path d="M12 2a10 10 0 1 0 0 20 10 10 0 0 0 0-20zm0 2c.9 1.2 1.6 2.9 1.9 5h-3.8c.3-2.1 1-3.8 1.9-5zM4.3 13a8 8 0 0 1 0-2h3.8a18 18 0 0 0 0 2zm.6 2h3.4c.3 1.5.8 2.8 1.4 3.8A8 8 0 0 1 4.9 15zm3.4-6H4.9a8 8 0 0 1 4.8-3.8c-.6 1-1.1 2.3-1.4 3.8zM12 20c-.9-1.2-1.6-2.9-1.9-5h3.8c-.3 2.1-1 3.8-1.9 5zm2-7h-4a16 16 0 0 1 0-2h4a16 16 0 0 1 0 2zm.3 5.8c.6-1 1.1-2.3 1.4-3.8h3.4a8 8 0 0 1-4.8 3.8zM15.9 13a18 18 0 0 0 0-2h3.8a8 8 0 0 1 0 2zm-.2-4c-.3-1.5-.8-2.8-1.4-3.8A8 8 0 0 1 19.1 9z"/></svg>
      </div>
    </div>
  </section>
</main>
</body>
</html>
```